2024 Comprehensive Needs Assessment

Design our 2024 Binder Report Cover. Front, Spine, Back. We are in the Education field, reporting data for strategic planning. I have attached our color palette and the previous years covers as a sample.

```html
<!DOCTYPE html>
<html lang="en">
<head>
<meta charset="utf-8">
<title>2024 Comprehensive Needs Assessment – Cover</title>
<link href="https://fonts.googleapis.com/css2?family=Oswald:wght@400;500;700&display=swap" rel="stylesheet">
<style>
  :root {
    --page-bg: #ebebeb;
    --cover-bg: #f7f7f6;
    --ink: #1c1c1c;
    --brand-red: #e8334a;
    --brand-peach: #e3ae98;
    --brand-blue: #3f86b7;
    --brand-green: #8cc63f;
    --art-light: #e9eef3;
    --art-warm: #d9824f;
    --art-cool: #46607c;
  }
  * { margin: 0; padding: 0; box-sizing: border-box; }
  html, body {
    width: 1200px; height: 1200px; overflow: hidden;
    background: var(--page-bg);
  }
  .cover {
    position: absolute;
    left: 240px; top: 40px;
    width: 720px; height: 1120px;
    background: var(--cover-bg);
    overflow: hidden;
    box-shadow: 0 10px 30px rgba(0,0,0,0.08);
  }
  .cover-graphics {
    position: absolute; inset: 0;
    width: 720px; height: 1120px;
  }
  .cover-title {
    position: absolute;
    left: 81px; top: 585px;
    font-family: "Oswald", sans-serif;
    white-space: nowrap;
  }
  .report-year {
    font-size: 52px; font-weight: 500;
    color: var(--ink); line-height: 1;
    letter-spacing: 1px;
  }
  .report-name {
    margin-top: 16px;
    font-size: 70px; font-weight: 700;
    color: var(--brand-red);
    line-height: 1;
    text-transform: uppercase;
    letter-spacing: 1px;
  }
  .district-name {
    margin-top: 12px;
    font-size: 25px; font-weight: 400;
    color: var(--ink);
    text-transform: uppercase;
    letter-spacing: 0.5px;
  }
  .publisher {
    position: absolute;
    left: 500px; top: 1040px;
    display: flex; align-items: center; gap: 10px;
    font-family: "Oswald", sans-serif;
    font-weight: 400; font-size: 24px; line-height: 1.05;
    color: var(--ink);
  }
  .publisher-dot {
    width: 22px; height: 22px; border-radius: 50%;
    background: var(--brand-green);
    flex: none;
  }
</style>
</head>
<body>
  <main class="cover">
    <svg class="cover-graphics" viewBox="0 0 720 1120" xmlns="http://www.w3.org/2000/svg">
      <defs>
        <linearGradient id="heroTone" x1="0" y1="0" x2="1" y2="1">
          <stop offset="0" stop-color="var(--art-light)"/>
          <stop offset="0.45" stop-color="var(--art-warm)" stop-opacity="0.75"/>
          <stop offset="1" stop-color="var(--art-cool)" stop-opacity="0.85"/>
        </linearGradient>
      </defs>

      <polygon class="hero-art" role="img"
        aria-label="Illustration of two analysts reviewing charts and dashboards on screens at a desk"
        points="0,0 720,0 720,195 330,520 0,268"
        fill="url(#heroTone)"/>

      <path class="band band-peach" d="M -30 282 L 290 528 Q 330 560 370 528 L 760 214"
        fill="none" stroke="var(--brand-peach)" stroke-width="56" stroke-linecap="butt"/>
      <path class="band band-red-top" d="M 300 508 L 372 562 Q 412 592 452 562 L 760 330"
        fill="none" stroke="var(--brand-red)" stroke-width="46" stroke-opacity="0.92"/>

      <path class="band band-blue" d="M -30 1070 L 110 925 Q 144 890 178 925 L 430 1180"
        fill="none" stroke="var(--brand-blue)" stroke-width="40"/>
      <path class="band band-red-bottom" d="M -30 905 L 40 905 Q 70 905 95 930 L 330 1185"
        fill="none" stroke="var(--brand-red)" stroke-width="36" stroke-opacity="0.92"/>
    </svg>

    <header class="cover-title">
      <p class="report-year">2024</p>
      <h1 class="report-name">Comprehensive<br>Needs Assessment</h1>
      <p class="district-name">Maplecrest School District</p>
    </header>

    <div class="publisher">
      <span class="publisher-dot"></span>
      <span class="publisher-name">Brightpath<br>Learning, LLC</span>
    </div>
  </main>
</body>
</html>
```